Lumo Vessa Wigs " Styling Foam"

I need a label created for my product . The bottle size is 50ml so it must be designed to fit that size bottle. I will post my logo and examples of my bottle size. I want the label design to be simple and cute. ill also add pictures of my website, so you can get ideas from there. The bottle is white so I want the main colors to be white and pink. All colors on the label must match my logo. I love glitter as well.

I know for sure I want my logo big, and I want "Styling Foam'',
then under styling foam I would like " Medium Hold" in a different front. be very creative.

Then under that I would like it to say " No Alcohol , Saulfate or Paraben

please make sure on the label in the front it has "NET: 7.0 oz / 200g" so people know what size it is.

I would like a glitter border on the label.

I also want the back of the label to have directions.

And ingredients list too . Very small not too big at all.

Target Market(s)

My target market is woman of all ages .. but mainly woman from ages 26-65

Industry/Entity Type

Hair And Beauty

Font styles to use
Serif
Sans Serif
Decorative
Script

Colors
e667a6
eda3c7
f9d9e8
e34297

Requirements
Must have
• The project must match the colors of my logo, it must have a nice pretty glitter border . It must be simple and clean . But still stylish ! I don’t want everything after my logo to be in the same font . Have fun with this design, be creative. My logo and “ Styling Foam” must be the two centerpiece!
Nice to have
• It will be nice to have different fonts! And nice to have all the colors that match my logo
Must be expensive looking !!
Very eye catching!
Should not have
• Do not add colors that my logo doesn’t have !!!!
I don’t want it to look too plain and boring ! I want it to be classy and expensive looking !

```html
<!DOCTYPE html>
<html lang="en">
<head>
<meta charset="utf-8">
<title>Lumo Vessa Wigs – Styling Foam Label</title>
<link rel="stylesheet" href="https://fonts.googleapis.com/css2?family=Oswald:wght@400;500&family=Lobster&family=Playfair+Display:wght@700&family=Tinos&display=swap">
<style>
  :root {
    --page: #ffffff;
    --label-white: #ffffff;
    --pink-band: #e8a7c7;
    --pink-soft: #f9d9e8;
    --pink-mid: #e667a6;
    --pink-deep: #e34297;
    --text-white: #ffffff;
    --glitter-light: #f2f2f4;
    --glitter-mid: #c9c9ce;
    --glitter-dark: #9a9aa2;
  }
  * { margin: 0; padding: 0; box-sizing: border-box; }
  html, body {
    width: 1200px;
    height: 1200px;
    overflow: hidden;
    background: var(--page);
  }
  .canvas {
    position: relative;
    width: 1200px;
    height: 1200px;
  }
  .label {
    position: absolute;
    left: 390px;
    top: 60px;
    width: 420px;
    height: 1080px;
    background: var(--label-white);
    overflow: hidden;
    box-shadow: 0 0 0 1px #eeeeee;
  }
  .label-art {
    position: absolute;
    inset: 0;
    width: 420px;
    height: 1080px;
  }
  .brand {
    position: absolute;
    left: 0;
    right: 0;
    top: 250px;
    text-align: center;
    font-family: "Playfair Display", serif;
    font-weight: 700;
    color: var(--pink-deep);
  }
  .brand-name {
    display: block;
    font-size: 60px;
    line-height: 1;
    letter-spacing: 1px;
  }
  .brand-sub {
    display: block;
    margin-top: 16px;
    font-size: 30px;
    line-height: 1;
    letter-spacing: 14px;
    padding-left: 14px;
  }
  .product-title {
    position: absolute;
    left: 0;
    right: 0;
    top: 560px;
    text-align: center;
    font-family: "Oswald", sans-serif;
    font-weight: 500;
    font-size: 80px;
    line-height: 86px;
    color: var(--text-white);
    letter-spacing: 1px;
  }
  .hold-pill {
    position: absolute;
    left: 80px;
    width: 260px;
    top: 762px;
    height: 50px;
    border-radius: 25px;
    background: var(--pink-deep);
    border: 2px solid var(--pink-soft);
    text-align: center;
    font-family: "Lobster", cursive;
    font-size: 30px;
    line-height: 44px;
    color: var(--text-white);
  }
  .claims {
    position: absolute;
    left: 0;
    right: 0;
    top: 836px;
    text-align: center;
    font-family: "Tinos", serif;
    font-size: 24px;
    line-height: 32px;
    color: var(--text-white);
  }
  .divider {
    position: absolute;
    left: 80px;
    width: 260px;
    top: 918px;
    height: 2px;
    background: var(--text-white);
  }
  .net-weight {
    position: absolute;
    left: 0;
    right: 0;
    top: 932px;
    text-align: center;
    font-family: "Tinos", serif;
    font-size: 21px;
    line-height: 26px;
    color: var(--text-white);
  }
</style>
</head>
<body>
<main class="canvas">
  <section class="label">
    <svg class="label-art" viewBox="0 0 420 1080" xmlns="http://www.w3.org/2000/svg">
      <defs>
        <linearGradient id="glitterTone" x1="0" y1="0" x2="1" y2="1">
          <stop offset="0" stop-color="var(--glitter-light)"/>
          <stop offset="0.35" stop-color="var(--glitter-mid)"/>
          <stop offset="0.6" stop-color="var(--glitter-light)"/>
          <stop offset="0.85" stop-color="var(--glitter-dark)"/>
          <stop offset="1" stop-color="var(--glitter-mid)"/>
        </linearGradient>
      </defs>
      <rect class="pink-band" x="0" y="520" width="420" height="560" fill="var(--pink-band)"/>
      <path class="glitter-top" role="img" aria-label="Silver glitter border"
            d="M0 0 H420 V100 C350 88 300 150 215 152 C135 154 70 118 0 140 Z"
            fill="url(#glitterTone)"/>
      <path class="glitter-bottom" role="img" aria-label="Silver glitter border"
            d="M0 1080 V990 C70 960 140 1012 220 1004 C300 996 350 950 420 958 V1080 Z"
            fill="url(#glitterTone)"/>
    </svg>

    <div class="brand">
      <span class="brand-name">Lumo Vessa</span>
      <span class="brand-sub">WIGS</span>
    </div>

    <h1 class="product-title">STYLING<br>FOAM</h1>

    <div class="hold-pill">Medium Hold</div>

    <p class="claims">No Alcohol<br>Saulfate &amp; Paraben Free</p>

    <div class="divider"></div>

    <p class="net-weight">NET: 7.0 oz / 200g</p>
  </section>
</main>
</body>
</html>
```